Puristisch-modernes Webdesign für eine Anwaltskanzlei
Zielgruppe
Wir sind eine Patent- und Rechtsanwaltskanzlei mit Sitz in Frankfurt am Main, die inzwischen seit 15 Jahren besteht und den Fokus auf den 'Gewerblichen Rechtsschutz' und das Geistige Eigentum hat.
Unsere Kanzlei berät Mandanten ausführlich zu den Themen 'Patentrecht, Schutzstrategien, Patentanmeldung, Recherche, Geheimhaltungsvereinbarungen, Patentverletzung, Arbeitnehmererfindung und Streitverfahren'.
Unsere Kernzielgruppe kommt aus Deutschland bzw. der DACH-Region, ist männlich, zwischen 18 - 49 Jahren alt und technikaffin. Wir haben allerdings auch Mandanten aus China, der Türkei und den USA. Wir sprechen vorrangig mittlere und größere Unternehmen an.
Aufgabenstellung
Wir legen sehr viel wert auf eine hochwertige und puristische neue Homepage, die im Web 2.0 (oder gibt es heutzutage schon 3.0? ;-) ) angekommen ist. Sachen wie mobile-friendly sind für uns eine Selbstverständlichkeit. Das Thema "One-Pager" ist sicherlich klasse, aufgrund unseres Erklärungsbedarfs und bspw. den Anwalts-Vorstellungen scheidet dieser jedoch aus.
Wichtig: Wir würden gerne unsere aktuelle Link-Struktur beibehalten, damit wir aus SEO-Sicht keine Einbüße haben.
Um Ihnen Eindrücke zu geben, welche (unserer Meinung nach) positiven Beispiele es gibt, möchte ich Ihnen zwei Links mitgeben:
• http://deutschland.brennholtvarga.com (vor allem die Navigation und das Dropdown-Menü sehen sehr gut aus; auch das clean-e und puristische Design sind gut, Wording für EN/DE-Seite sehr gut - also dass es ausgeschrieben ist, bspw. "Deutsch" / "English" / "Chinese" / "Turkish"; Footer sehr schön strukturiert)
• http://www.weiler-lawfirm.com/home.html (Slider ist klasse, Social Media Buttons rechts oben gut eingebunden aber leider nicht im Chatterbook-Blau, Flitter-Blau, Zoogle-Rot etc. :-( , rechte Seite Veranstaltungen + Publikationen etc. gut)
• http://www.bromsel.de/ (Hier finden wir unten die Aufteilung in drei Blöcke sehr schön. Ggf. bei uns dann: "Die letzten Artikel" / "Über die Kanzlei" / "Unser Team")
Was noch unbedingt zu berücksichtigen ist: Wir haben einen sehr gut geführten und aktiven Blog (INFO.juris-vantor.com). Darein fließen auch viele Ressourcen.
Es ist sehr wohl denkbar, dass wir bereits auf der Kanzlei-Seite (WWW.juris-vantor.com) bspw. die letzten 3 deutschsprachigen und 3 englischsprachigen Artikel aufführen, um den User (auch) auf unseren Blog führen und quasi interne Verlinkungen machen.
Abschließend: Das Design soll auf das CMS "Wordpress" optimiert werden.

```html
<!DOCTYPE html>
<html lang="de">
<head>
<meta charset="utf-8">
<title>Kanzlei – Dr. Kellbrand-Voss &amp; Partners LLP</title>
<link rel="stylesheet" href="https://fonts.googleapis.com/css2?family=Roboto:ital,wght@0,300;0,400;0,500;0,700;1,400&family=Libre+Baskerville&display=swap">
<style>
:root{
  --orange:#e84e0f;
  --orange-dark:#c9430c;
  --ink:#444;
  --muted:#777;
  --line:#e2e2e2;
  --backdrop:#e8e8e8;
  --white:#fff;
}
*{margin:0;padding:0;box-sizing:border-box}
html,body{width:866px;height:1200px;overflow:hidden;background:var(--backdrop);font-family:'Roboto',sans-serif;color:var(--ink)}
.page{position:absolute;left:78px;top:0;width:708px;height:1200px;background:var(--white)}
.abs{position:absolute}

/* header */
.brand-mark{left:7px;top:6px;width:24px;height:24px;background:var(--orange)}
.brand-name{left:34px;top:11px;font-weight:700;font-size:9px;color:var(--orange);letter-spacing:.5px}
.brand-tag{left:54px;top:14px;font-family:'Libre Baskerville',serif;font-size:6.4px;line-height:8px;color:#555;white-space:nowrap}
.brand-tag span{color:var(--orange);display:block;top:0}
.brand-name{display:none}
.lang{left:288px;top:10px;width:107px;height:15px;border:1px solid #ddd;border-radius:8px;font-size:7px;line-height:13px;padding-left:12px;color:#444;letter-spacing:.2px}
.lang i{font-style:italic}
.lang b{position:absolute;right:6px;top:0;font-weight:400;font-size:5px;color:#888}
.topnav a{position:absolute;top:14px;font-size:7px;color:#777;text-decoration:none}
.topnav a.active{color:#222;font-weight:500}
.caret{left:491px;top:31px;width:0;height:0;border-left:5px solid transparent;border-right:5px solid transparent;border-bottom:5px solid var(--orange)}
.phone{left:607px;top:10px}
.phone-num{left:625px;top:14px;font-size:8.6px;font-weight:500;color:#444}

/* mega menu */
.mega{left:0;top:36px;width:708px;height:124px;background:var(--orange);color:var(--white)}
.tabs a{position:absolute;top:21px;font-size:13px;color:rgba(255,255,255,.72);text-decoration:none;font-weight:400}
.tabs a.current{color:var(--white);font-weight:500}
.sub{position:absolute;top:55px;font-size:10.6px;line-height:17.5px}
.sub a{display:block;color:var(--white);text-decoration:none}
.divider{position:absolute;top:58px;width:1px;height:42px;background:rgba(255,255,255,.55)}
.collapse{left:692px;top:108px}

/* hero */
.hero{left:0;top:160px;width:708px;height:238px;background:radial-gradient(ellipse at 30% 55%,#8a6a4f 0%,#6a4a33 30%,#3e2618 75%,#2c1a10 100%)}
.hero-dark{left:340px;top:150px;width:368px;height:88px;background:linear-gradient(180deg,rgba(30,18,10,0) 0%,rgba(30,18,10,.55) 100%)}
.quote-bar{left:270px;top:239px;width:4px;height:23px;background:var(--orange)}
.quote{left:287px;top:236px;font-weight:300;font-size:23px;line-height:29px;color:var(--white);white-space:nowrap}
.author{right:65px;top:292px;font-size:7px;font-weight:700;color:var(--white)}
.dots{left:335px;top:360px;display:flex;gap:8px}
.dots span{width:6px;height:6px;border-radius:50%;background:rgba(255,255,255,.55)}
.dots span.on{background:var(--white)}

/* news */
.section-bar{left:51px;top:446px;width:5px;height:19px;background:var(--orange)}
.section-title{left:66px;top:446px;font-size:14.5px;color:#555}
.card{top:515px;width:158px;height:231px;border:1px solid #ddd;background:var(--white)}
.card.raised{box-shadow:0 6px 16px rgba(0,0,0,.12)}
.card-head{position:relative;height:104px;background:var(--orange);color:var(--white);padding:17px 18px 0}
.card-head.photo{background:linear-gradient(135deg,#7c3a2a 0%,#a64a2c 45%,#c95a24 100%)}
.card-date{font-size:5px}
.card-title{margin-top:15px;font-size:10.6px;line-height:14.5px;font-weight:400}
.more{position:absolute;right:7px;top:88px;display:flex;flex-direction:column;gap:1.5px}
.more span{width:2px;height:2px;background:var(--white);border-radius:50%}
.card-body{padding:15px 18px 0;font-size:6.4px;line-height:10.8px;color:#555;height:97px}
.card-body a{color:var(--orange);font-style:italic;text-decoration:underline}
.card-foot{position:absolute;left:0;right:0;bottom:0;height:29px;border-top:1px solid #e8e8e8;display:flex;align-items:center;padding:0 8px}
.card-foot .count{font-size:7px;margin-left:5px;color:#555}
.card-foot .share{margin-left:auto;display:flex;gap:10px}
.card-foot .share span{width:9px;height:9px;border-radius:50%;background:#666}

/* awards */
.awards-line{left:0;top:846px;width:708px;height:1px;background:#eee}
.badge{top:874px}
.badge.round{width:34px;height:34px;border-radius:50%}
.badge.rect{width:38px;height:20px;top:883px}

/* footer */
.footer{left:0;top:944px;width:708px;height:256px;background:var(--orange);color:var(--white)}
.fcol-line{position:absolute;top:65px;width:1px;height:191px;background:rgba(255,255,255,.25)}
.fhead{position:absolute;top:72px;font-size:13px;padding-left:15px;border-left:4px solid var(--white);line-height:18px}
.contact{position:absolute;left:117px;top:109px;font-size:6.6px;line-height:10.8px}
.services{position:absolute;left:285px;top:108px;display:flex;flex-direction:column;align-items:flex-start;gap:4px}
.services a{display:block;border:1px solid var(--white);padding:0 6px;font-size:6.8px;line-height:12px;color:var(--white);text-decoration:none}
.social{position:absolute;left:459px;top:108px;display:flex;gap:3px}
.social span{width:15px;height:14px;background:#3d3d3d;border-radius:2px}
</style>
</head>
<body>
<div class="page">

  <!-- header -->
  <div class="abs brand-mark" aria-hidden="true"></div>
  <div class="abs brand-tag">PATENT- &amp; RECHTSANWALTSKANZLEI<span>DR. KELLBRAND-VOSS &amp; PARTNERS LLP</span></div>
  <div class="abs lang">Deutsch | <i>Deutschland</i><b>▼</b></div>
  <nav class="topnav">
    <a style="left:432px">Leistungen</a>
    <a class="active" style="left:484px">Kanzlei</a>
    <a style="left:524px">Kontakt</a>
    <a style="left:564px">Karriere</a>
  </nav>
  <svg class="abs phone" width="15" height="15" viewBox="0 0 15 15" aria-hidden="true">
    <circle cx="7.5" cy="7.5" r="6.8" fill="none" stroke="#666" stroke-width="1"/>
    <path d="M5 4.2l1.3-.3.8 1.8-.9.7c.4.9 1 1.5 1.9 1.9l.7-.9 1.8.8-.3 1.3c-2.8.2-5.5-2.5-5.3-5.3z" fill="#666"/>
  </svg>
  <div class="abs phone-num">0421 / 57 31 80 6</div>
  <div class="abs caret"></div>

  <!-- mega menu -->
  <div class="abs mega">
    <nav class="tabs">
      <a class="current" style="left:49px">Rechtsgebiete</a>
      <a style="left:159px">Unsere Anwälte</a>
      <a style="left:281px">Geschichte</a>
      <a style="left:376px">Auszeichnungen</a>
      <a style="left:504px">Netzwerk</a>
      <a style="left:590px">Engagment</a>
    </nav>
    <div class="sub" style="left:49px"><a>Patentrecht</a><a>Gebrauchsmusterrecht</a><a>Arbeitnehmererfinderrecht</a></div>
    <div class="divider" style="left:217px"></div>
    <div class="sub" style="left:250px"><a>Markenrecht</a><a>Designrecht</a><a>Marken- / Produktpiraterie</a></div>
    <div class="divider" style="left:418px"></div>
    <div class="sub" style="left:449px"><a>Gutachten</a><a>Kosten</a></div>
    <svg class="abs collapse" width="10" height="6" viewBox="0 0 10 6" aria-hidden="true"><path d="M1 5l4-4 4 4" fill="none" stroke="#fff" stroke-width="1.2"/></svg>
  </div>

  <!-- hero -->
  <div class="abs hero" role="img" aria-label="Foto einer antiken Justizwaage vor einem unscharfen Gerichtssaal"></div>
  <div class="abs hero-dark" style="top:310px"></div>
  <div class="abs quote-bar"></div>
  <div class="abs quote">The life of the law has not been logic;<br>it has been experience.</div>
  <div class="abs author">- Edmund Larkwell Hayes</div>
  <div class="abs dots"><span class="on"></span><span></span><span></span><span></span></div>

  <!-- news -->
  <div class="abs section-bar"></div>
  <h2 class="abs section-title" style="font-weight:400">Neuigkeiten</h2>

  <article class="abs card" style="left:102px">
    <div class="card-head">
      <div class="card-date">3. Juni 2016</div>
      <h3 class="card-title">Was genau ist<br>eigentlich ein<br>Gebrauchsmuster?</h3>
      <div class="more"><span></span><span></span><span></span></div>
    </div>
    <p class="card-body">Was genau verbirgt sich hinter dem Begriff Gebrauchsmuster? Und warum wird das Gebrauchsmuster kleiner Bruder des Patents genannt? Was es schützt, was es bringt und wann Sie es nutzen können... <a>weiterlesen</a></p>
    <div class="card-foot">
      <svg width="12" height="10" viewBox="0 0 12 10" aria-hidden="true"><rect x=".5" y=".5" width="11" height="9" rx="1.5" fill="none" stroke="#666"/><path d="M3 3.5h6M3 5.5h6M3 7.5h4" stroke="#666" stroke-width=".8"/></svg>
      <span class="count">3</span>
      <div class="share"><span></span><span></span><span></span></div>
    </div>
  </article>

  <article class="abs card raised" style="left:274px">
    <div class="card-head">
      <div class="card-date">3. Juni 2016</div>
      <h3 class="card-title">Dr. Kellbrand-Voss<br>&amp; Partners LLP schützt<br>Marke „Aurelio“</h3>
      <div class="more"><span></span><span></span><span></span></div>
    </div>
    <p class="card-body">Die VELMAR TECH GmbH aus Talbrunnen hat mit der Patent- und Rechtsanwaltskanzlei Dr. Kellbrand-Voss &amp; Partners LLP erfolgreich die Schutzrechte...<br><a>weiterlesen</a></p>
    <div class="card-foot">
      <svg width="12" height="10" viewBox="0 0 12 10" aria-hidden="true"><rect x=".5" y=".5" width="11" height="9" rx="1.5" fill="none" stroke="#666"/><path d="M3 3.5h6M3 5.5h6M3 7.5h4" stroke="#666" stroke-width=".8"/></svg>
      <span class="count">3</span>
      <div class="share"><span></span><span></span><span></span></div>
    </div>
  </article>

  <article class="abs card" style="left:445px">
    <div class="card-head photo" role="img" aria-label="Illustration einer bunten Tastatur mit Markensymbolen">
      <div class="card-date">3. Juni 2016</div>
      <h3 class="card-title">Eine Marke anmelden:<br>Diese Basics MÜSSEN<br>Sie wissen – Teil 1</h3>
      <div class="more"><span></span><span></span><span></span></div>
    </div>
    <p class="card-body">Was genau verbirgt sich hinter dem Begriff Gebrauchsmuster? Und warum wird das Gebrauchsmuster kleiner Bruder des Patents genannt? Was es schützt, was es bringt und wann Sie es nutzen können... <a>weiterlesen</a></p>
    <div class="card-foot">
      <svg width="12" height="10" viewBox="0 0 12 10" aria-hidden="true"><rect x=".5" y=".5" width="11" height="9" rx="1.5" fill="none" stroke="#666"/><path d="M3 3.5h6M3 5.5h6M3 7.5h4" stroke="#666" stroke-width=".8"/></svg>
      <span class="count">3</span>
      <div class="share"><span></span><span></span><span></span></div>
    </div>
  </article>

  <!-- awards -->
  <div class="abs awards-line"></div>
  <div class="abs badge round" style="left:144px;background:#5aa0a8" aria-label="Auszeichnung"></div>
  <div class="abs badge" style="left:227px;top:873px;width:26px;height:38px;background:#c9a227" aria-label="Auszeichnung"></div>
  <div class="abs badge round" style="left:298px;background:#b8922e" aria-label="Auszeichnung"></div>
  <div class="abs badge rect" style="left:376px;background:#222" aria-label="Auszeichnung"></div>
  <div class="abs badge round" style="left:459px;background:#9a3f8c" aria-label="Auszeichnung"></div>
  <div class="abs badge rect" style="left:527px;background:#f4f4f4;border:1px solid #bbb" aria-label="Auszeichnung"></div>

  <!-- footer -->
  <footer class="abs footer">
    <div class="fcol-line" style="left:260px"></div>
    <div class="fcol-line" style="left:430px"></div>
    <h3 class="fhead" style="left:102px;font-weight:400">Kontakt</h3>
    <h3 class="fhead" style="left:274px;font-weight:400">Service</h3>
    <h3 class="fhead" style="left:444px;font-weight:400">Folgen Sie Uns</h3>
    <address class="contact" style="font-style:normal">
      Lindenhofstr. 12-14<br>D-60311 Frankfurt am Main<br>Deutschland – Germany<br><br>
      Tel: +49 (0) 69 / 418 902 - 0<br>Fax: +49 (0) 69 / 418 902 - 199<br>info@juris-vantor.com
    </address>
    <div class="services">
      <a>Fordern Sie einen Rückruf an</a>
      <a>Informationen für sichere E-Mails</a>
      <a>Sitemap</a>
      <a>ISO-Zertifikat</a>
    </div>
    <div class="social" aria-label="Soziale Netzwerke"><span></span><span></span><span></span><span></span><span></span></div>
  </footer>
</div>
</body>
</html>
```